The book title is:

The Quietly Capable Schedule Keeper

Ewan Holloway, MSc, MBA, PMP

It is a book about professional yet common sense project management principles aimed at beginner to experienced project managers. The book is written in a conversational, informal tone with reference to best practice in project management. It is designed to be used as an accessible desk reference. I am looking for a cover design that is striking, eye catching, and professional. It can have an element of fun and informality to reflect the tone of the contents.

I have attached a copy of the draft manuscript so you can get a feel for what the book is like.

see www.taskguildnet.org for more about the profession of project management

Target Market(s)

Professional Project Managers of all levels (see www.taskguildnet.org for further information)

Industry/Entity Type

Management

Requirements
Must have
• Must be suitable for 6" x 9" book size

```html
<!DOCTYPE html>
<html lang="en">
<head>
<meta charset="utf-8">
<title>The Quietly Capable Schedule Keeper — Cover</title>
<link href="https://fonts.googleapis.com/css2?family=Fira+Sans+Condensed:wght@600;700&display=swap" rel="stylesheet">
<style>
  :root {
    --stage: #e9e9ec;
    --cover-navy: #2b2080;
    --cover-deep: #1d1560;
    --spine: #251b72;
    --violet: #7a2fc0;
    --magenta: #c23ad8;
    --ember: #e2571e;
    --title-white: #ffffff;
    --title-shadow: rgba(10, 6, 40, 0.85);
    --rule: rgba(220, 220, 255, 0.75);
  }
  * { margin: 0; padding: 0; box-sizing: border-box; }
  html, body {
    width: 1200px;
    height: 900px;
    overflow: hidden;
    background: var(--stage);
  }
  .canvas {
    position: relative;
    width: 1200px;
    height: 900px;
  }
  .cover {
    position: absolute;
    left: 293px;
    top: 60px;
    width: 614px;
    height: 780px;
    background: var(--cover-navy);
    overflow: hidden;
    font-family: "Fira Sans Condensed", "Arial Narrow", sans-serif;
    box-shadow: 0 10px 28px rgba(0, 0, 0, 0.28);
  }
  .cover-art {
    position: absolute;
    left: 98px;
    top: 240px;
    right: 0;
    bottom: 70px;
    background:
      radial-gradient(circle at 62% 30%, rgba(140, 210, 255, 0.55) 0 60px, transparent 120px),
      radial-gradient(ellipse at 25% 78%, rgba(226, 87, 30, 0.7) 0, transparent 45%),
      radial-gradient(ellipse at 50% 50%, rgba(194, 58, 216, 0.65) 0, transparent 60%),
      linear-gradient(160deg, var(--cover-navy) 0%, var(--violet) 45%, var(--cover-deep) 100%);
  }
  .spine {
    position: absolute;
    left: 0;
    top: 0;
    width: 98px;
    height: 100%;
    background: var(--spine);
    border-right: 1px solid rgba(255, 255, 255, 0.08);
  }
  .spine-title {
    position: absolute;
    left: 36px;
    top: 194px;
    writing-mode: vertical-rl;
    color: var(--title-white);
    font-weight: 700;
    font-size: 19px;
    letter-spacing: 0.2px;
    white-space: nowrap;
  }
  .title {
    position: absolute;
    right: 48px;
    top: 26px;
    text-align: right;
    color: var(--title-white);
    font-weight: 700;
    font-size: 58px;
    line-height: 69px;
    text-shadow: 3px 4px 0 var(--title-shadow), 0 0 6px rgba(0, 0, 0, 0.4);
  }
  .title-rule {
    position: absolute;
    left: 123px;
    top: 245px;
    width: 464px;
    height: 2px;
    background: linear-gradient(90deg, transparent, var(--rule) 20%, var(--rule) 80%, transparent);
  }
  .author {
    position: absolute;
    left: 158px;
    top: 736px;
    color: var(--title-white);
    font-weight: 700;
    font-size: 16px;
    letter-spacing: 0.2px;
  }
</style>
</head>
<body>
<main class="canvas">
  <section class="cover">
    <div class="cover-art" role="img" aria-label="Hand holding a glowing striped globe amid purple and orange light streaks"></div>
    <div class="spine">
      <p class="spine-title">The Quietly Capable Schedule Keeper</p>
    </div>
    <h1 class="title">The Quietly<br>Capable<br>Schedule Keeper</h1>
    <div class="title-rule"></div>
    <p class="author">Ewan Holloway, MSc, MBA, PMP</p>
  </section>
</main>
</body>
</html>
```